Design a corporate looking website for Harbourline Funding

Need design only WordPress mock up for Harbourline Funding who provides short term finance solutions to other businesses. We need a corporate looking website that depicts a trustworthy, Dynamic fast acting company.
Visit http://k7.pagelantern-demo.net/ for current mock up We need something like e this but not the same with a design that depicts corporate with more colour and images, needs to install trust and fast action. Please feel free to change the layout as I am not wedded to current design but am happy with what on the landing page.

Target Market(s)

Small to medium sized Businesses

Industry/Entity Type

Finance

Number of Pages Required

1 page

Font styles to use
Sans Serif

Requirements
Must have
• Design Landing pages in WordPress
• Visit http://k7.pagelantern-demo.net/ for current mock up need Layout like this but with a design that depicts corporate with more colour and images, needs to install trust and fast action. Please feel free to change the layout as I am not happy with current design but am wedded to what on the landing page.
Should not have
• any copyright material on it.

```html
<!DOCTYPE html>
<html lang="en">
<head>
<meta charset="utf-8">
<title>Harbourline Funding</title>
<link href="https://fonts.googleapis.com/css2?family=Roboto:ital,wght@0,400;0,500;1,400&family=Quicksand:wght@500&family=Lora:ital@1&display=swap" rel="stylesheet">
<style>
:root{
  --ink:#2b3440;
  --muted:#6f7781;
  --navy:#16365f;
  --navy-deep:#0f2440;
  --accent:#1f8fc4;
  --action:#f07f1f;
  --teal:#1aa59a;
  --line:#e1e6ec;
  --page:#f7f9fb;
  --tint:#eaf3f9;
}
*{box-sizing:border-box;margin:0;padding:0}
html,body{width:708px;height:1200px;overflow:hidden;background:var(--page)}
body{font-family:'Roboto',Arial,sans-serif;color:var(--ink)}
.site{width:1200px;height:2034px;transform:scale(.59);transform-origin:0 0;position:relative;background:var(--page);overflow:hidden}
.abs{position:absolute}
p{font-size:12px;line-height:19px;color:var(--muted)}
.serif-sub{font-family:'Lora',Georgia,serif;font-style:italic;color:var(--accent);font-size:14px;white-space:nowrap}
.media{border-radius:3px}
.media-hero{background:linear-gradient(135deg,#16365f 0%,#1f8fc4 60%,#7cc4e4 100%)}
.media-team{background:linear-gradient(135deg,#1f8fc4,#1aa59a)}
.media-a{background:linear-gradient(135deg,#16365f,#2f6aa3)}
.media-b{background:linear-gradient(135deg,#1aa59a,#7fd1c6)}
.media-c{background:linear-gradient(135deg,#f07f1f,#f6b46a)}
.btn{display:inline-block;border:1px solid #d6dde5;background:#fff;border-radius:3px;font-size:13px;color:var(--muted);padding:7px 14px;white-space:nowrap}
.btn-action{background:var(--action);border-color:var(--action);color:#fff}
.btn-navy{background:var(--navy);border-color:var(--navy);color:#fff}
.divider{position:absolute;left:100px;width:1000px;height:1px;background:var(--line)}
.topbar{left:0;top:0;width:1200px;height:38px;background:var(--navy-deep);color:#d7e2ee;font-size:12px}
.topbar span{position:absolute;top:12px;white-space:nowrap}
.header{left:0;top:38px;width:1200px;height:90px;background:#fff;border-bottom:3px solid var(--accent)}
.brand{left:112px;top:66px;width:288px;height:82px;background:#fff;display:flex;align-items:center;gap:12px;padding-left:18px}
.brand-mark{width:26px;height:26px;border-radius:50%;background:var(--action);flex:none}
.brand-name{font-size:22px;font-weight:500;color:var(--navy);white-space:nowrap}
.nav{left:537px;top:71px;display:flex;align-items:center;font-size:14px}
.nav a{color:#5b6570;text-decoration:none;padding:6px 18px;border-right:1px solid #dfe4ea}
.nav a:last-child{border:none}
.nav .active{background:var(--navy);color:#fff;border-radius:3px;border:none;margin-right:10px}
.hero-title{left:720px;top:160px;font-family:'Quicksand',sans-serif;color:var(--accent);font-size:29px;line-height:33px;font-weight:500}
.feature h3{font-size:16px;font-weight:500;color:var(--ink);margin-bottom:6px;white-space:nowrap}
.icon-wrap{width:40px;height:40px;border-radius:50%;display:flex;align-items:center;justify-content:center}
.quote-band{left:100px;top:677px;width:1000px;height:86px;background:var(--tint);border-left:4px solid var(--action);text-align:center;font-size:17px;color:var(--navy);padding-top:24px;line-height:21px}
.social-mini{display:flex;gap:10px}
.social-mini i{width:16px;height:16px;background:#b9c7d6;border-radius:2px;display:block}
.testi{border:1px solid var(--line);border-top:3px solid var(--accent);background:#fff;padding:22px 24px;font-style:italic;font-size:12px;line-height:18px;color:#7b838c;box-shadow:0 2px 3px rgba(0,0,0,.06)}
.footer{left:0;top:1686px;width:1200px;height:296px;background:var(--navy-deep);color:#c6d3e2}
.footer h4{font-weight:400;font-size:18px;color:#fff}
.footer ul{list-style:none;font-size:12px}
.footer li{border-bottom:1px solid #24406a;padding:10px 0;height:36px}
.field{background:#1a3457;border:1px solid #2a4a74;font-size:11px;color:#9fb2c8;padding:8px}
.base{left:0;top:1982px;width:1200px;height:52px;background:#0a1a30;color:#c6d3e2;font-size:12px}
.sq{width:24px;height:24px;border-radius:3px;display:inline-block}
</style>
</head>
<body>
<div class="site">

  <div class="abs topbar">
    <span style="left:102px">&#9990; Call Us: +1 555 014 72 90</span>
    <span style="left:892px">Follow us: <i style="display:inline-block;width:11px;height:11px;background:#5aa9d6;vertical-align:middle"></i> <i style="display:inline-block;width:11px;height:11px;background:#4a6aa8;vertical-align:middle"></i> <i style="display:inline-block;width:11px;height:11px;background:var(--action);vertical-align:middle"></i></span>
    <span style="left:1055px"><i style="display:inline-block;width:8px;height:8px;border-radius:50%;background:var(--action)"></i> Login</span>
  </div>
  <div class="abs header"></div>
  <div class="abs brand"><span class="brand-mark"></span><span class="brand-name">Harbourline Funding</span></div>
  <nav class="abs nav">
    <a class="active">Home</a><a>About Us</a><a>Services</a><a>Gallery</a><a>Blog</a><a>Contacts</a>
  </nav>

  <svg class="abs" style="left:64px;top:295px" width="20" height="26"><path d="M16 2 6 13l10 11" fill="none" stroke="#9fb2c8" stroke-width="3"/></svg>
  <svg class="abs" style="left:1118px;top:295px" width="20" height="26"><path d="M4 2l10 11L4 24" fill="none" stroke="#9fb2c8" stroke-width="3"/></svg>
  <div class="abs" style="left:100px;top:162px;width:589px;height:289px;background:#fff;border:1px solid var(--line);padding:4px;box-shadow:0 8px 12px -8px rgba(0,0,0,.25)">
    <div class="media media-hero" role="img" aria-label="Slideshow photo of business owners closing a fast finance deal" style="width:100%;height:100%;border-radius:0"></div>
  </div>
  <div class="abs" style="left:353px;top:419px;width:88px;height:22px;background:#fff;border-radius:4px;display:flex;gap:4px;align-items:center;justify-content:center">
    <i style="width:10px;height:10px;border-radius:50%;background:var(--action)"></i><i style="width:10px;height:10px;border-radius:50%;background:#dde3ea"></i><i style="width:10px;height:10px;border-radius:50%;background:#dde3ea"></i><i style="width:10px;height:10px;border-radius:50%;background:#dde3ea"></i><i style="width:10px;height:10px;border-radius:50%;background:#dde3ea"></i>
  </div>
  <h1 class="abs hero-title">Unique Morden Concepts<br>for<br>Coperate Businness</h1>
  <p class="abs" style="left:720px;top:274px;width:380px">Lorem Ipsum. Proin gravida nibh vel velit auctor aliquet. Aenean sollici-tudin, lorem quis bibendum auctor, Proin gravida nibh vel velit</p>
  <p class="abs" style="left:720px;top:347px;width:380px">Lorem Ipsum. Proin gravida nibh vel velit auctor aliquet. Aenean sollici-tudin, lorem quis bibendum auctor, Proin gravida nibh vel velit</p>
  <span class="abs btn btn-action" style="left:720px;top:409px;font-size:17px;padding:10px 12px">Read more &nbsp;|&nbsp; &#10140;</span>

  <div class="divider" style="top:490px"></div>

  <div class="abs feature" style="left:100px;top:520px;width:310px">
    <div class="abs icon-wrap" style="left:0;top:0;background:var(--navy)"><svg width="24" height="24" viewBox="0 0 24 24"><circle cx="12" cy="12" r="10" fill="none" stroke="#fff" stroke-width="2"/><path d="M2 12h20M12 2v20" stroke="#fff" stroke-width="1.6"/></svg></div>
    <div style="margin-left:54px"><h3>Long established fact that.</h3><div class="serif-sub">Many variations of passages.</div></div>
    <p style="margin-top:10px">Lorem Ipsum. Proin gravida nibh vel velit auctor aliquet. Aenean sollicitudin, lorem quis bibendum auctor, Proin gravida nibh vel velit</p>
  </div>
  <div class="abs feature" style="left:447px;top:520px;width:310px">
    <div class="abs icon-wrap" style="left:0;top:0;background:var(--teal)"><svg width="24" height="24" viewBox="0 0 24 24"><circle cx="12" cy="12" r="8" fill="none" stroke="#fff" stroke-width="4" stroke-dasharray="3.2 2"/><circle cx="12" cy="12" r="3" fill="#fff"/></svg></div>
    <div style="margin-left:51px"><h3>Content of a page when</h3><div class="serif-sub">Been the industry's standard.</div></div>
    <p style="margin-top:10px">Lorem Ipsum. Proin gravida nibh vel velit auctor aliquet. Aenean sollicitudin, lorem quis bibendum auctor, Proin gravida nibh vel velit</p>
  </div>
  <div class="abs feature" style="left:791px;top:520px;width:309px">
    <div class="abs icon-wrap" style="left:0;top:0;background:var(--action)"><svg width="24" height="24" viewBox="0 0 24 24"><rect x="2" y="3" width="20" height="14" rx="1.5" fill="none" stroke="#fff" stroke-width="2"/><path d="M8 21h8M12 17v4" stroke="#fff" stroke-width="2"/></svg></div>
    <div style="margin-left:54px"><h3>Many variations of passages</h3><div class="serif-sub">Randomised words which.</div></div>
    <p style="margin-top:10px">Lorem Ipsum. Proin gravida nibh vel velit auctor aliquet. Aenean sollicitudin, lorem quis bibendum auctor, Proin gravida nibh vel velit</p>
  </div>

  <div class="abs quote-band">&ldquo; Lorem Ipsum. Proin gravida nibh vel velit auctor aliquet. Aenean sollicitudin, lorem quis<br>bibendum auctor, Proin gravida nibh vel velit . &rdquo;</div>
  <svg class="abs" style="left:166px;top:708px" width="16" height="26"><path d="M13 2 4 13l9 11" fill="none" stroke="#9fb2c8" stroke-width="3"/></svg>
  <svg class="abs" style="left:1018px;top:708px" width="16" height="26"><path d="M3 2l9 11-9 11" fill="none" stroke="#9fb2c8" stroke-width="3"/></svg>

  <div class="abs media media-team" role="img" aria-label="Photo of the funding team advising a client" style="left:100px;top:805px;width:270px;height:163px"></div>
  <h2 class="abs" style="left:398px;top:802px;font-size:18px;font-weight:400;color:var(--navy)">What we do?</h2>
  <p class="abs" style="left:398px;top:823px;white-space:nowrap">Lorem Ipsum. Proin gravida nibh vel velit auctor aliquet. Aenean sollici</p>
  <p class="abs" style="left:398px;top:853px;width:360px;text-align:justify">Lorem Ipsum. Proin gravida nibh vel velit auctor aliquet. Aenean sollicitudin, lorem quis bibendum auctor, Proin gravida nibh vel velit</p>
  <p class="abs" style="left:398px;top:910px;width:360px;text-align:justify">Lorem Ipsum. Proin gravida nibh vel velit auctor aliquet. Aenean sollicitudin, lorem quis bibendum auctor, Proin gravida nibh vel velit Lorem Ipsum. Proin gravida nibh vel velit auctor aliquet. Aenean sollicitudin, lorem quis bibendum auctor, Proin gravida nibh vel velit</p>
  <p class="abs" style="left:791px;top:853px;width:310px;text-align:justify">Lorem Ipsum. Proin gravida nibh vel velit auctor aliquet. Aenean sollicitudin, lorem quis bibendum auctor, Proin gravida nibh vel velit</p>
  <span class="abs btn btn-navy" style="left:791px;top:956px">Read more</span>
  <span class="abs btn" style="left:889px;top:956px">Get in touch</span>

  <div class="divider" style="top:1018px"></div>

  <div class="abs media media-a" role="img" aria-label="Photo for working capital loans" style="left:100px;top:1058px;width:309px;height:159px"></div>
  <div class="abs media media-b" role="img" aria-label="Photo for invoice finance" style="left:447px;top:1058px;width:309px;height:159px"></div>
  <div class="abs media media-c" role="img" aria-label="Photo for fast bridging finance" style="left:791px;top:1058px;width:309px;height:159px"></div>
  <p class="abs" style="left:100px;top:1233px;width:305px;text-align:justify">Lorem Ipsum. Proin gravida nibh vel velit auctor aliquet. Aenean sollicitudin, lorem quis bibendum auctor, Proin gravida nibh vel velit Lorem Ipsum. Proin gravida nibh vel velit auctor aliquet. Aenean sollicitudin, lorem quis biben-dum auctor, Proin gravida nibh vel velit</p>
  <p class="abs" style="left:447px;top:1233px;width:305px;text-align:justify;color:#4f5862">Lorem Ipsum. Proin gravida nibh vel velit auctor aliquet. Aenean sollicitudin, lorem quis bibendum auctor, Proin gravida nibh vel velit Lorem Ipsum. Proin gravida nibh vel velit auctor aliquet. Aenean sollicitudin, lorem quis biben-dum auctor, Proin gravida nibh vel velit</p>
  <p class="abs" style="left:791px;top:1233px;width:305px;text-align:justify;color:#4f5862">Lorem Ipsum. Proin gravida nibh vel velit auctor aliquet. Aenean sollicitudin, lorem quis bibendum auctor, Proin gravida nibh vel velit Lorem Ipsum. Proin gravida nibh vel velit auctor aliquet. Aenean sollicitudin, lorem quis biben-dum auctor, Proin gravida nibh vel velit</p>
  <span class="abs btn" style="left:100px;top:1349px">Read more</span>
  <span class="abs btn" style="left:447px;top:1349px">Read more</span>
  <span class="abs btn" style="left:791px;top:1349px">Read more</span>
  <div class="abs social-mini" style="left:336px;top:1356px"><i></i><i></i><i></i></div>
  <div class="abs social-mini" style="left:683px;top:1356px"><i></i><i></i><i></i></div>
  <div class="abs social-mini" style="left:1028px;top:1356px"><i></i><i></i><i></i></div>

  <div class="divider" style="top:1411px"></div>

  <h2 class="abs" style="left:100px;top:1444px;font-size:18px;font-weight:400;color:var(--navy)">Testimonials</h2>
  <div class="abs serif-sub" style="left:100px;top:1469px">Scrambled it to make a type specimen book.</div>
  <div class="abs testi" style="left:100px;top:1500px;width:309px;height:100px">Simply dummy text of the printing and typesetting industry. Lorem Ipsum has been the industry's standard dummy text ever since.</div>
  <div class="abs testi" style="left:447px;top:1500px;width:309px;height:100px">Established fact that a reader will be distracted by the readable content of a page when looking at its layout.</div>
  <div class="abs" style="left:232px;top:1609px;font-size:12px;white-space:nowrap"><span style="color:var(--accent)">Mara Elwin</span>, Web Designer</div>
  <div class="abs" style="left:558px;top:1609px;font-size:12px;white-space:nowrap"><span style="color:var(--accent)">Tomas Reyl</span>, Flash Developer</div>

  <h2 class="abs" style="left:791px;top:1444px;font-size:18px;font-weight:400;color:var(--navy)">Newsletter</h2>
  <div class="abs serif-sub" style="left:791px;top:1469px">Content of a page when looking.</div>
  <p class="abs" style="left:791px;top:1495px">There are many variations of passages of Lorem.</p>
  <div class="abs" style="left:791px;top:1526px;width:222px;height:31px;border:1px solid #d6dde5;background:#fff;font-size:11px;color:#8a929b;padding:9px 10px;white-space:nowrap">Please enter your E-mail addres</div>
  <span class="abs btn btn-action" style="left:1017px;top:1526px">Subscribe</span>
  <p class="abs" style="left:791px;top:1568px;width:300px;line-height:17px">Many variations of passages of Lorem Ipsum available, but the majority have suffered alteration.</p>

  <footer class="abs footer">
    <div class="abs" style="left:104px;top:9px;width:215px;height:61px;background:#fff;display:flex;align-items:center;gap:8px;padding-left:12px">
      <span style="width:18px;height:18px;border-radius:50%;background:var(--action);flex:none"></span><span style="font-size:16px;font-weight:500;color:var(--navy);white-space:nowrap">Harbourline Funding</span>
    </div>
    <div class="abs" style="left:106px;top:81px;width:280px;font-size:12px;line-height:21px;color:#fff;font-weight:500;letter-spacing:-.4px">Lorem Ipsum. Proin gravida nibh vel velit auctor aliquet. Aenean sollicitudin, lorem quis bibendum auctor, nisi elit consequat ipsum, nec sagittis sem nibh id elit. Duis sed odio sit amet nibh vulputate cursus a sit amet maaliquam massa nisl quis neque. Suspendisse in orci enim.</div>
    <h4 class="abs" style="left:440px;top:26px">Navigation</h4>
    <ul class="abs" style="left:440px;top:66px;width:160px">
      <li>Home</li><li>&rsaquo; About Us</li><li>Services</li><li>Gallery</li><li>Blog</li><li style="border:none">Contacts</li>
    </ul>
    <h4 class="abs" style="left:614px;top:26px">Categories</h4>
    <ul class="abs" style="left:614px;top:66px;width:178px">
      <li>Web design</li><li>&rsaquo; Illustrations</li><li>HTML Coding</li><li>Icons</li><li>Flash Animation</li><li style="border:none">3D Design</li>
    </ul>
    <h4 class="abs" style="left:830px;top:26px">Get in touch</h4>
    <div class="abs" style="left:829px;top:71px;width:260px;font-size:12px;line-height:16px">Established fact that a reader will be distracted by the readable content of a page.</div>
    <div class="abs field" style="left:829px;top:120px;width:133px;height:28px">Name</div>
    <div class="abs field" style="left:967px;top:120px;width:133px;height:28px">E-mail</div>
    <div class="abs field" style="left:829px;top:154px;width:271px;height:73px">Message</div>
    <span class="abs btn btn-action" style="left:829px;top:236px;padding:6px 10px">Send message &#9993;</span>
    <span class="abs" style="left:1020px;top:243px;font-size:12px;white-space:nowrap">Or call us now</span>
  </footer>
  <div class="abs base">
    <span class="abs" style="left:100px;top:19px">Copyright &copy; 2016</span>
    <span class="abs" style="left:858px;top:19px;color:#fff">Follow Us:</span>
    <div class="abs" style="left:930px;top:14px;display:flex;gap:5px">
      <span class="sq" style="background:#e8edf2"></span><span class="sq" style="background:#4a6aa8"></span><span class="sq" style="background:#3b5998"></span><span class="sq" style="background:#e8edf2"></span><span class="sq" style="background:var(--action)"></span><span class="sq" style="background:#5ab4e0"></span>
    </div>
  </div>

</div>
</body>
</html>
```